Umgestaltung eines bestehenden DIN lang Wickelfalz-Flyers  für Arbeitgeberverband Fitness
Umgestaltung eines bestehenden DIN lang Wickelfalz-Flyers für Arbeitgeberverband Fitness
Zielgruppe
Wir sind ein spezialisierter Versicherungsmakler. Wir bieten Sonderkonzepte für die Geschäftsversicherungen von Fitness- und Gesundheitsanlagen.
Wir sind eine Kooperation mit einem Arbeitgeberverband für Gesundheits- und Fitnessstudios eingegangen und brauchen für die Verbandsmitglieder einen Flyer.
Unsere Homepage: www.brenkemakler.com
Aufgabenstellung
Umgestaltung eines 6-seitigen DIN lang Flyers, Wickelfalz. Der bisherige Flyer ist als PDF angehängt. Mittlerweile besitzen wir ein neues Logo ( angehängt ). Der neue Flyer soll aufgrund einer Kooperation mit einem Verband ( www.vtakr.de ) umgestaltet werden.
Der Verband bekommt von uns exklusive Sonderleistungen für seine Verbandsmitglieder geboten. Das Logo (angehängt) vom Verband soll ebenfalls mit eingearbeitet werden .
Wir suchen nach einem frischen, modernen Design mit passenden Bildmaterial. Bildvorschläge sollten von euch kommen ( bevorzugt www.bildquarz.de). Die Bildrechte werden von uns außerhalb dieser Ausschreibung vom Lizenzgeber erworben. DIN lang Format und inhaltliche Strukturen sollten annähernd beibehalten werden. Textvorschäge liegen als Word Dokument bei, können jedoch bei Bedarf auch abgeändert werden.
Eine 2. Ausschreibung für einen anderen Verband ( Fitnesstrainer) erfolgt zeitgleich auf "gestaltwerkstatt", bitte schaut auch diese Ausschreibung an, da der 2. Flyer nachezu identisch wie dieser hier werden soll.

```html
<!DOCTYPE html>
<html lang="de">
<head>
<meta charset="utf-8">
<title>Flyer VTAKR – Brenke &amp; Partner</title>
<link rel="stylesheet" href="https://fonts.googleapis.com/css2?family=PT+Sans+Narrow:wght@400;700&display=swap">
<style>
  :root {
    --green: #1e9a3c;
    --green-dark: #177a2f;
    --grey-dark: #4a4a4a;
    --grey-mid: #8c8c8c;
    --grey-light: #d9d9d9;
    --text: #333333;
    --paper: #ffffff;
  }
  html, body { margin: 0; padding: 0; overflow: hidden; background: var(--paper); }
  .flyer {
    position: relative; width: 1200px; height: 853px; overflow: hidden;
    background: var(--paper); color: var(--text);
    font-family: "PT Sans Narrow", "Arial Narrow", sans-serif;
  }
  .art { position: absolute; inset: 0; }
  .panel { position: absolute; top: 0; height: 853px; }

  /* left panel */
  .tagline-diagonal {
    position: absolute; left: 10px; top: 480px; width: 520px;
    transform-origin: left top; transform: rotate(-45deg);
    font-size: 27px; color: var(--green); white-space: nowrap; letter-spacing: 0.2px;
  }
  .competence {
    position: absolute; left: 150px; top: 428px; width: 246px;
    text-align: right; font-size: 15px; line-height: 18px;
  }
  .competence h2 { margin: 0 0 16px; font-size: 19px; color: var(--green-dark); }
  .competence p { margin: 0 0 14px; }
  .competence strong { color: var(--green); }
  .association-mark {
    position: absolute; left: 48px; top: 734px; width: 134px;
    text-align: center; font-size: 34px; font-weight: 700; color: var(--grey-dark);
  }
  .special-box {
    position: absolute; left: 192px; top: 714px; width: 208px; height: 68px;
    background: var(--grey-dark); color: var(--paper); text-align: center;
  }
  .special-box .title { font-size: 23px; font-weight: 700; margin-top: 8px; }
  .special-box .sub { font-size: 13px; font-weight: 700; }

  /* middle panel */
  .middle { left: 432px; width: 370px; }
  .headline {
    margin: 44px 0 0; font-size: 29px; line-height: 34px; font-weight: 700; color: var(--grey-dark);
  }
  .headline .accent { color: var(--green); }
  .headline .line2 { display: block; padding-left: 34px; }
  .section { margin-top: 22px; font-size: 15px; line-height: 19px; }
  .section h3 { margin: 0 0 2px; font-size: 17px; color: var(--green-dark); }
  .section p { margin: 0; }
  .section.highlight p { color: var(--green); }
  .middle .first { margin-top: 28px; }

  /* right panel */
  .right { left: 832px; width: 340px; }
  .offer-title { margin: 30px 0 0; font-size: 41px; line-height: 36px; font-weight: 700; color: var(--grey-dark); }
  .offer-title span { display: block; padding-left: 58px; color: var(--green-dark); }
  .offer-intro { margin: 42px 0 18px; font-size: 12px; }
  .offer-intro strong { color: var(--green); }
  .offer-list { list-style: none; margin: 0; padding: 0; }
  .offer-list li { margin-bottom: 17px; font-size: 10.5px; line-height: 13px; }
  .offer-list h4 { margin: 0 0 1px; font-size: 12.5px; color: var(--green-dark); }
</style>
</head>
<body>
<div class="flyer">
  <svg class="art" width="1200" height="853" viewBox="0 0 1200 853">
    <defs>
      <linearGradient id="photoLeft" x1="0" y1="0" x2="1" y2="1">
        <stop offset="0" stop-color="#d9c3a6"/>
        <stop offset="0.5" stop-color="#e8d6c4"/>
        <stop offset="1" stop-color="#ffffff" stop-opacity="0"/>
      </linearGradient>
      <linearGradient id="photoRight" x1="0" y1="0" x2="1" y2="1">
        <stop offset="0" stop-color="#8a8a86"/>
        <stop offset="0.6" stop-color="#e7e5e1"/>
        <stop offset="1" stop-color="#f4f2ef"/>
      </linearGradient>
    </defs>
    <!-- left photo area -->
    <rect x="0" y="0" width="414" height="560" fill="url(#photoLeft)" role="img" aria-label="Foto: junge Frau beim Hanteltraining im Fitnessstudio"/>
    <polygon points="0,0 120,0 0,120" fill="var(--green)"/>
    <polygon points="200,0 300,0 300,100" fill="var(--grey-mid)" opacity="0.7"/>
    <polygon points="300,0 414,0 414,230 300,100" fill="var(--grey-light)" opacity="0.8"/>
    <polygon points="120,170 270,70 270,130 150,210" fill="var(--grey-mid)" opacity="0.5"/>
    <polygon points="0,560 0,700 300,400 300,260" fill="var(--paper)" opacity="0.6"/>
    <!-- logo circle -->
    <circle cx="114" cy="752" r="86" fill="var(--green)"/>
    <circle cx="120" cy="748" r="76" fill="var(--paper)"/>
    <!-- right photo area -->
    <polygon points="826,853 1200,320 1200,853" fill="url(#photoRight)" role="img" aria-label="Foto: junger Mann beim Training an einem Fitnessgerät"/>
    <polygon points="1120,330 1200,318 1200,380 1150,380" fill="var(--green)"/>
    <polygon points="826,853 1200,318 1200,340 846,853" fill="var(--grey-dark)" opacity="0.8"/>
    <polygon points="1160,610 1200,560 1200,720" fill="var(--green)" opacity="0.85"/>
  </svg>

  <div class="tagline-diagonal">Kooperation Exklusivität Marktführung Ersparnis Leistung</div>

  <section class="competence">
    <h2>Kompetenz</h2>
    <p>Als <strong>Versicherungs-<br>makler</strong> und Leasing-<br>vermittler mit <strong>langjähriger<br>Erfahrung</strong>, begleiten und betreuen<br>wir <strong>objektiv</strong> und partnerschaftlich Ihre<br>Interessen in allen Versicherungs- und<br>Leasingbelangen.</p>
    <p>Persönliche und <strong>kompetente Beratung</strong>,<br>qualifiziertes Know-how sowie eine<br>unproblematische Schadensabwicklung sind<br>für uns der Garant für eine <strong>langfristige<br>Geschäftsbeziehung</strong> mit Ihnen.</p>
  </section>

  <div class="association-mark">VTAKR</div>
  <div class="special-box">
    <div class="title">Sonderkonditionen</div>
    <div class="sub">für VTAKR-Verbandsmitglieder</div>
  </div>

  <main class="panel middle">
    <h1 class="headline">Kooperation <span class="accent">Exklusivität</span><span class="line2"><span class="accent">Marktführung</span> Ersparnis <span class="accent">Leistung</span></span></h1>

    <section class="section first">
      <h3>Kooperation</h3>
      <p>Der VTAKR hat mit der Brenke &amp; Partner Unternehmensgruppe, bestehend aus einem spezialisierten Versicherungsmakler- und einem unabhängigen Leasingvermittlerunternehmen eine exklusive Kooperation geschlossen.</p>
    </section>
    <section class="section highlight">
      <h3>Exklusivität</h3>
      <p>Ausschließlich für Verbandsmitglieder des VTAKR wurde ein einzigartiger Rahmenvertrag, für Geschäftsversicherungen sowie für den Bereich Leasing-/ Finanzierungen verhandelt.</p>
    </section>
    <section class="section">
      <h3>Marktführung</h3>
      <p>Mit mehr als 1.300 bundesweit versicherten Fitness- und Gesundheitsanlagen, sowie ca. 2000 Betriebsstandorten aus der Freizeitindustrie, zählt die Brenke &amp; Partner Unternehmensgruppe zu den absolut spezialisierten und erfolgreichen Marktführern dieser Branchen.</p>
    </section>
    <section class="section highlight">
      <h3>Ersparnis</h3>
      <p>Für Verbandsmitglieder des VTAKR, bietet diese Kooperation die außergewöhnliche Möglichkeit der extremen Beitragsersparnis. Das Einsparpotenzial bei der Betriebsversicherung liegt bei bis zu 50% und weicht damit erheblich vom marktüblichen Niveau ab. Auch für den Bereich Leasing bzw. Finanzierung gelten Sonderkonditionen für den VTAKR.</p>
    </section>
    <section class="section">
      <h3>Leistung</h3>
      <p>Der Rahmenvertrag für die Geschäftsversicherung, bietet eine „Allgefahrenlösung“ für die betrieblichen Risiken in nur einem Vertrag an. Als Betreiber einer Fitness- oder Gesundheitsanlage, findet sowohl der Einzelbetreiber als auch der Filialist ein optimal auf seinen Bedarf maßgeschneiderten Versicherungsschutz bzw. Leasingvertrag.</p>
    </section>
  </main>

  <aside class="panel right">
    <h2 class="offer-title">Unser<span>Angebot</span></h2>
    <p class="offer-intro">Die <strong>„All-In-Risiko-Lösung“</strong> bietet in folgenden Bereichen Schutz:</p>
    <ul class="offer-list">
      <li><h4>Schutz der Sachwerte</h4>U.a.: Feuer, Einbruchdiebstahl, Vandalismus infolge Einbruch sowie Raub, Leitungswasser, Sturm und Hagel, Überspannung durch Blitz, innere Unruhe, böswillige Beschädigung, unbenannte Gefahren</li>
      <li><h4>Ertragsausfallversicherungen</h4>Ersetzt im Schadenfall die entgangenen Einnahmen</li>
      <li><h4>Betriebshaftpflicht</h4>Umfassender Versicherungsschutz gegenüber Schadenersatz- und Regressansprüchen, inkl. Privathaftpflicht</li>
      <li><h4>Glasversicherung</h4>Innen- und Außenverglasung ohne Flächenbegrenzung</li>
      <li><h4>Elektronikversicherung</h4>Alle Elektronikgeräte: Fitness-, Kardio-, EMS-geräte, PC, Bürotechnik und Beschallung</li>
      <li><h4>Elementarschäden</h4>Überschwemmung, Erdbeben, Erdrutsch, Schneedruck, Lawinen,<br>Vulkanausbruch, Rückstau</li>
      <li><h4>+ Optional</h4>Firmenrechtsschutz und / oder Gebäudeversicherung</li>
      <li><h4>+ Optional</h4>Leasing-/Mietkaufverträge</li>
    </ul>
  </aside>
</div>
</body>
</html>
```